Label Design VelmoRest Capsules

Hello dear designers!

We run a brand for dietary supplements and are looking for a talented designer to help take our brand to the next level. We are planning to launch new products with fresh packaging and redesigned labels. Additionally, we would like to refresh our company logo to make it fit better on the packaging.

Important Info:

Our brand: VelmoPure – specializing in products for detoxification, sleep, and eye protection.
Our shop: www.velmopure.at – currently offering two main products:
VelmoPure (Detox Tincture)
Velmo Optic Guard (Blue Light Filter Glasses)
Project Goal: Initially, we are looking for a label design for our new product VelmoRest (sleep capsules). If we like the design, we would like to revise the label for our first product, VelmoPure, and potentially rework our logo to make it more compact and visually appealing on our packaging.

Design Preferences: We are fans of the design style of Farv Nutra and would love a design in a similar style – modern, clean, and premium – but with a unique touch that fits our brand. You will find some inspirations and ideas that we particularly like in the attachment.

Important:

Our packaging for VelmoRest is an 8 OZ jar (similar to the smaller jars used by Farv Nutra).
The label should be clear, appealing, and give the product a high-quality look.
An example of a previous design draft (which hasn’t fully convinced us yet), along with inspirations for our upcoming bundle (including VelmoPure, VelmoRest, and VelmoOptic Guard), is also attached.
Special Opportunity: The designer with the best concept will have the chance to collaborate with us long-term! We have two more brands in the pipeline and are looking for a reliable and creative partner for future projects. Generous compensation and tips are guaranteed.

We look forward to seeing creative and professional designs that will take our brand to the next level!

Target Market(s)

Germany

Industry/Entity Type

Supplement

Font styles to use
Sans Serif

Colors

Designer to choose colors to be used in the design.

Requirements
Must have
• Es sollte Hochwertig und Modern aussehen. Matt schwarzer hintergrund. less is more
Nice to have
• Maybe The head should be visible in the background.
Should not have
• it should not be colorful, and not too playful, it should definitely not look cheap!

```html
<!DOCTYPE html>
<html lang="de">
<head>
<meta charset="utf-8">
<title>VelmoRest Label</title>
<link href="https://fonts.googleapis.com/css2?family=Poppins:wght@400;500;600&display=swap" rel="stylesheet">
<style>
  :root {
    --page-bg: #e4e4e4;
    --label-black: #151515;
    --label-black-deep: #0f0f0f;
    --panel-graphite: #232323;
    --panel-edge: #2e2e2e;
    --text-white: #f2f2f2;
    --text-soft: #c9c9c9;
    --accent-blue: #5aafd6;
    --bullet-bar: #5aafd6;
  }
  * { margin: 0; padding: 0; box-sizing: border-box; }
  html, body {
    width: 1200px;
    height: 1200px;
    overflow: hidden;
    background: var(--page-bg);
    font-family: "Poppins", sans-serif;
  }
  .label {
    position: absolute;
    left: 160px;
    top: 135px;
    width: 880px;
    height: 930px;
    background: linear-gradient(160deg, var(--label-black) 0%, var(--label-black-deep) 100%);
    overflow: hidden;
  }
  .brand-notch {
    position: absolute;
    left: 50%;
    top: 0;
    width: 290px;
    height: 230px;
    transform: translateX(-50%);
    background: var(--panel-graphite);
    border: 1px solid var(--panel-edge);
    border-top: none;
    border-radius: 0 0 145px 145px;
    display: flex;
    justify-content: center;
    padding-top: 92px;
  }
  .brand-name {
    color: var(--text-white);
    font-size: 27px;
    font-weight: 500;
    letter-spacing: 1px;
  }
  .product-title {
    position: absolute;
    left: 0;
    right: 0;
    top: 290px;
    text-align: center;
    color: var(--text-white);
    font-size: 112px;
    font-weight: 500;
    letter-spacing: 1px;
    line-height: 1;
  }
  .product-claim {
    position: absolute;
    left: 0;
    right: 0;
    top: 420px;
    text-align: center;
    color: var(--text-soft);
    font-size: 30px;
    font-weight: 400;
    letter-spacing: 0.5px;
  }
  .benefit-list {
    position: absolute;
    left: 275px;
    top: 590px;
    list-style: none;
  }
  .benefit-list li {
    color: var(--text-white);
    font-size: 34px;
    line-height: 54px;
    display: flex;
    align-items: center;
  }
  .benefit-list li::before {
    content: "";
    display: inline-block;
    width: 2px;
    height: 30px;
    background: var(--bullet-bar);
    margin-right: 12px;
  }
  .info-band {
    position: absolute;
    left: 20px;
    right: 20px;
    bottom: 25px;
    height: 125px;
    background: var(--panel-graphite);
    border: 1px solid var(--panel-edge);
    border-radius: 16px;
    text-align: center;
    padding-top: 16px;
  }
  .info-type {
    display: inline-block;
    color: var(--accent-blue);
    font-size: 30px;
    letter-spacing: 0.5px;
    padding: 0 14px 4px;
    border-bottom: 2px solid var(--accent-blue);
  }
  .info-amount {
    color: var(--accent-blue);
    font-size: 29px;
    letter-spacing: 0.5px;
    margin-top: 6px;
  }
</style>
</head>
<body>
  <div class="label">
    <div class="brand-notch">
      <span class="brand-name">VELMOPURE</span>
    </div>
    <h1 class="product-title">VELMO REST</h1>
    <p class="product-claim">FÖRDERT DIE TIEFSCHLAFPHASE</p>
    <ul class="benefit-list">
      <li>Untertitel hinzufügen</li>
      <li>Untertitel hinzufügen</li>
      <li>Untertitel hinzufügen</li>
    </ul>
    <div class="info-band">
      <div class="info-type">NAHRUNGSERGÄNZUNGSMITTEL</div>
      <div class="info-amount">30 PORTIONEN | 60 KAPSELN</div>
    </div>
  </div>
</body>
</html>
```